Re-branding for Structural Engineering firm

We need new business cards as part of our current re-branding. We have a new logo (attached), so the card design should incorporate this color scheme. We are a structural engineering firm providing structural building design and seismic consulting services. The final design should communicate professionalism and stability, with a modern look and feel.

```html
<!DOCTYPE html>
<html lang="en">
<head>
<meta charset="UTF-8">
<title>Northbeam Structural Engineering – Business Card</title>
<link href="https://fonts.googleapis.com/css2?family=Montserrat:wght@400;500;700&display=swap" rel="stylesheet">
<style>
  :root {
    --brand-blue: #1f6db5;
    --brand-grey: #8a8b8d;
    --card-white: #ffffff;
    --backdrop: #e9ebee;
  }
  html, body {
    margin: 0;
    padding: 0;
    width: 1200px;
    height: 1200px;
    overflow: hidden;
    background: var(--backdrop);
    font-family: "Montserrat", sans-serif;
  }
  .card {
    position: absolute;
    left: 100px;
    top: 314px;
    width: 1000px;
    height: 572px;
    background: var(--card-white);
    box-shadow: 0 10px 30px rgba(0,0,0,0.15);
    overflow: hidden;
  }
  .card-band {
    position: absolute;
    left: 0;
    bottom: 0;
    width: 1000px;
    height: 200px;
  }
  .brand {
    position: absolute;
    left: 150px;
    top: 120px;
    width: 300px;
    color: var(--brand-blue);
    font-weight: 700;
  }
  .brand-square {
    width: 150px;
    height: 150px;
    background: var(--brand-blue);
    margin-bottom: 18px;
  }
  .brand-name {
    font-size: 34px;
    letter-spacing: 1px;
    line-height: 1.1;
    margin: 0;
  }
  .brand-tagline {
    font-size: 22px;
    letter-spacing: 1px;
    line-height: 1.15;
    margin: 6px 0 0;
  }
  .divider {
    position: absolute;
    left: 500px;
    top: 70px;
    width: 2px;
    height: 300px;
    background: var(--brand-blue);
  }
  .contact {
    position: absolute;
    left: 540px;
    top: 70px;
    color: var(--brand-blue);
  }
  .person-name {
    font-size: 34px;
    font-weight: 700;
    margin: 0;
    line-height: 1.1;
  }
  .person-title {
    font-size: 20px;
    font-weight: 500;
    margin: 2px 0 0 28px;
  }
  .address {
    font-size: 18px;
    line-height: 1.35;
    margin: 22px 0 0 70px;
  }
  .contact-list {
    list-style: none;
    padding: 0;
    margin: 12px 0 0 70px;
    font-size: 19px;
  }
  .contact-list li {
    display: flex;
    align-items: center;
    gap: 14px;
    height: 38px;
  }
  .contact-list svg {
    width: 20px;
    height: 20px;
    fill: var(--brand-blue);
    flex: none;
  }
</style>
</head>
<body>
  <div class="card">
    <svg class="card-band" viewBox="0 0 1000 200" preserveAspectRatio="none">
      <path d="M600 110 C780 95 900 60 1000 20 L1000 45 C900 80 780 105 600 110 Z" fill="var(--brand-grey)"/>
      <path d="M0 120 L600 112 C780 105 900 80 1000 45 L1000 200 L0 200 Z" fill="var(--brand-blue)"/>
    </svg>

    <div class="brand">
      <div class="brand-square"></div>
      <p class="brand-name">NORTHBEAM</p>
      <p class="brand-tagline">STRUCTURAL<br>ENGINEERING</p>
    </div>

    <div class="divider"></div>

    <div class="contact">
      <p class="person-name">Lena Marsh, S.E.</p>
      <p class="person-title">Principal</p>
      <p class="address">4100 Harbor View Dr., Ste 210<br>Bayport, CA 92000</p>
      <ul class="contact-list">
        <li>
          <svg viewBox="0 0 24 24"><path d="M6.6 10.8a15.1 15.1 0 0 0 6.6 6.6l2.2-2.2a1 1 0 0 1 1-.25 11.4 11.4 0 0 0 3.6.57 1 1 0 0 1 1 1V20a1 1 0 0 1-1 1A17 17 0 0 1 3 4a1 1 0 0 1 1-1h3.5a1 1 0 0 1 1 1c0 1.25.2 2.45.57 3.57a1 1 0 0 1-.25 1z"/></svg>
          555.310.4821
        </li>
        <li>
          <svg viewBox="0 0 24 24"><path d="M3 7c0-1.5 4-3 9-3s9 1.5 9 3v2h-4V7.5c-1.5-.4-3-.5-5-.5s-3.5.1-5 .5V9H3z"/><path d="M5 11h14l1 9H4z"/><circle cx="12" cy="15.5" r="2.5" fill="#fff"/></svg>
          555.310.4822
        </li>
        <li>
          <svg viewBox="0 0 24 24"><path d="M2 5h20v14H2z"/><path d="M2 5l10 8 10-8" fill="none" stroke="#fff" stroke-width="1.6"/></svg>
          lena@northbeamse.com
        </li>
        <li>
          <svg viewBox="0 0 24 24"><circle cx="12" cy="12" r="10"/><path d="M2 12h20M12 2c3 3 3 17 0 20M12 2c-3 3-3 17 0 20" fill="none" stroke="#fff" stroke-width="1.4"/></svg>
          www.northbeamse.com
        </li>
      </ul>
    </div>
  </div>
</body>
</html>
```